Simple, Professional and neat business card design for Vendralo Inc.

We're looking to re-vamp our business card design. We're a supplier of innovative feed ingredients for the North American animal agriculture industry. We are located in Lucknow, Ontario, Canada and our flagship product is a product that prevents milk fever in dairy cows when the calve, it is fed before calving and is very effective compared to other alternatives available on the market today.

Our company has Danish roots and we import all of our product from our Danish partner/manufacturer in Denmark. We like our design to embrace high professionalism while remaining neat and simple.

Target Market(s)

B2B, Feed Mills, Veterinary Clinics, Large integrators/producers,

Industry/Entity Type

Agribusiness

Contact Information for Business Card

We like the rounded corners because they make the card easy to sit in a wallet and not many use it so it makes the card stand out, just possibly something to take account for during the design.

As you can also see on the sliders below, looking for a that simple but proffesional scandinavian design.

Requirements
Nice to have
• Rounded corners
Should not have
• Too vibrant

```html
<!DOCTYPE html>
<html lang="en">
<head>
<meta charset="utf-8">
<title>Vendralo Inc. — Business Card</title>
<link rel="stylesheet" href="https://fonts.googleapis.com/css2?family=Roboto:wght@400;500&family=Roboto+Condensed:wght@400;700&family=Lato:wght@900&display=swap">
<style>
  :root {
    --bg: #2b2b2b;
    --card: #f3f3f3;
    --blue: #1a5aa6;
    --divider: #1a5aa6;
    --text: #4f4f4f;
    --label: #555555;
  }
  * { box-sizing: border-box; margin: 0; padding: 0; }
  html, body { width: 1200px; height: 960px; overflow: hidden; }
  body { background: var(--bg); position: relative; font-family: "Roboto", Arial, sans-serif; }

  .card {
    position: absolute;
    width: 600px;
    height: 343px;
    background: var(--card);
    border-radius: 22px;
    box-shadow: 0 4px 10px rgba(0,0,0,.45);
  }
  .card--front { left: 314px; top: 113px; }
  .card--back  { left: 311px; top: 472px; }

  .brand { position: absolute; display: flex; align-items: center; gap: 12px; }
  .brand__dot { width: 40px; height: 40px; border-radius: 50%; background: var(--blue); flex: none; }
  .brand__name { font-family: "Lato", Arial, sans-serif; font-weight: 900; color: var(--blue); font-size: 25px; line-height: 30px; letter-spacing: -.2px; }
  .card--front .brand { left: 44px; top: 50px; }

  .contact { position: absolute; left: 44px; top: 147px; color: var(--text); font-size: 14.5px; line-height: 18px; font-style: normal; }
  .contact__address { margin-bottom: 9px; }
  .contact__row { display: flex; align-items: center; gap: 7px; height: 19px; }
  .contact__row svg { width: 13px; height: 13px; fill: var(--blue); flex: none; }

  .holder { position: absolute; right: 46px; top: 215px; font-family: "Roboto Condensed", Arial, sans-serif; font-weight: 700; color: var(--blue); font-size: 22px; }

  .card--back .brand { left: 0; right: 0; top: 40px; flex-direction: column; gap: 8px; }
  .card--back .brand__dot { width: 62px; height: 62px; }

  .tagline { position: absolute; left: 0; right: 0; top: 158px; text-align: center; font-family: "Roboto Condensed", Arial, sans-serif; font-weight: 700; color: var(--blue); font-size: 24.5px; line-height: 24px; }

  .features { position: absolute; left: 90px; top: 226px; display: flex; align-items: stretch; }
  .feature { width: 143px; display: flex; flex-direction: column; align-items: center; gap: 6px; }
  .feature svg { width: 64px; height: 64px; }
  .feature__label { font-family: "Roboto Condensed", Arial, sans-serif; font-size: 14.5px; color: var(--label); }
  .feature + .feature { border-left: 1.5px solid var(--divider); }
</style>
</head>
<body>

<section class="card card--front">
  <div class="brand">
    <span class="brand__dot"></span>
    <span class="brand__name">VENDRALO INC.</span>
  </div>

  <address class="contact">
    <div class="contact__address">Box 724, Harrowfield<br>Ontario Canada N0X 3K1</div>
    <div class="contact__row"><svg viewBox="0 0 24 24"><path d="M6.6 10.8a15 15 0 0 0 6.6 6.6l2.2-2.2c.3-.3.7-.4 1-.2 1.1.4 2.3.6 3.6.6.6 0 1 .4 1 1V20c0 .6-.4 1-1 1A17 17 0 0 1 3 4c0-.6.4-1 1-1h3.5c.6 0 1 .4 1 1 0 1.3.2 2.5.6 3.6.1.3 0 .7-.2 1z"/></svg>888-604-2719 (TF)</div>
    <div class="contact__row"><svg viewBox="0 0 24 24"><path d="M6.6 10.8a15 15 0 0 0 6.6 6.6l2.2-2.2c.3-.3.7-.4 1-.2 1.1.4 2.3.6 3.6.6.6 0 1 .4 1 1V20c0 .6-.4 1-1 1A17 17 0 0 1 3 4c0-.6.4-1 1-1h3.5c.6 0 1 .4 1 1 0 1.3.2 2.5.6 3.6.1.3 0 .7-.2 1z"/></svg>519-440-3186</div>
    <div class="contact__row"><svg viewBox="0 0 24 24"><path d="M7 1h10a2 2 0 0 1 2 2v18a2 2 0 0 1-2 2H7a2 2 0 0 1-2-2V3a2 2 0 0 1 2-2zm0 3v15h10V4z"/></svg>519-772-0948</div>
    <div class="contact__row"><svg viewBox="0 0 24 24"><path d="M6 2h12v6H6zM3 9h18a2 2 0 0 1 2 2v7h-4v4H5v-4H1v-7a2 2 0 0 1 2-2zm4 8v3h10v-3z"/></svg>519-440-3190</div>
    <div class="contact__row"><svg viewBox="0 0 24 24"><path d="M2 5h20v14H2zm2 2v.5l8 5 8-5V7z"/></svg>mads@vendralo.com</div>
    <div class="contact__row"><svg viewBox="0 0 24 24"><path d="M12 2a10 10 0 1 0 0 20 10 10 0 0 0 0-20zm-1 17.9A8 8 0 0 1 4.2 10L9 15v1a2 2 0 0 0 2 2zm6.9-2.5A2 2 0 0 0 16 16h-1v-3a1 1 0 0 0-1-1H8v-2h2a1 1 0 0 0 1-1V7h2a2 2 0 0 0 2-2v-.4a8 8 0 0 1 2.9 12.8z"/></svg>www.vendralo.com</div>
  </address>

  <div class="holder">MADS KJELDSEN</div>
</section>

<section class="card card--back">
  <div class="brand">
    <span class="brand__dot"></span>
    <span class="brand__name">VENDRALO INC.</span>
  </div>

  <p class="tagline">Distributor of innovative fed ingredients<br>&amp; other preventative health products.</p>

  <div class="features">
    <div class="feature">
      <svg viewBox="0 0 64 64" fill="none" stroke="var(--blue)" stroke-width="4">
        <path d="M32 4 L56 12 V32 C56 46 45 55 32 60 C19 55 8 46 8 32 V12 Z"/>
        <circle cx="32" cy="30" r="11" fill="var(--blue)" stroke="none"/>
        <path d="M32 24v12M26 30h12" stroke="#fff" stroke-width="3"/>
      </svg>
      <span class="feature__label">Preventative Care</span>
    </div>
    <div class="feature">
      <svg viewBox="0 0 64 64" fill="none" stroke="var(--blue)" stroke-width="4" stroke-linecap="round">
        <path d="M14 50 A26 26 0 1 1 56 40" stroke-dasharray="2 6"/>
        <path d="M32 32 L44 14"/>
        <path d="M14 56 L30 40 L38 46 L56 28"/>
        <path d="M46 28 H56 V38"/>
      </svg>
      <span class="feature__label">High-performance</span>
    </div>
    <div class="feature">
      <svg viewBox="0 0 64 64" fill="none" stroke="var(--blue)" stroke-width="4">
        <circle cx="32" cy="32" r="28"/>
        <text x="32" y="42" text-anchor="middle" font-family="Roboto Condensed, Arial, sans-serif" font-weight="700" font-size="28" fill="var(--blue)" stroke="none">Rx</text>
        <path d="M12 12 L52 52"/>
      </svg>
      <span class="feature__label">prescription-free</span>
    </div>
  </div>
</section>

</body>
</html>
```